New website for Fribrix.se - self employment agency for freelance workers

[NOTE THE CODED ADD-ON HAS BEEN INCLUDED ALREADY (DC ADMIN)] New layout based on Wordpress themes including migration of existing content at fribrix.se. Want to use existing logotype as guideline for total layout concept. Please use existing structure and text content on fribrix.se. Existing pictures are optional to reuse. The secured part of the existing website under "Logga in" is not part of this project.

Target Market(s)

Self employment within all industries and ages above 16.

Industry/Entity Type

Finance And Accounting

Font styles to use
Other font styles liked:
• Should match with logotype

Colors
3176b5
85abd2
cfdeed

Requirements
Must have
• Ready to use wordpress themes. Include salary calculation bar as in existing website. Multi lingual ready(today only in Swedish). Mobile client responsive.

```html
<!DOCTYPE html>
<html lang="sv">
<head>
<meta charset="utf-8">
<title>Fribrix – Fakturera utan eget företag</title>
<link rel="stylesheet" href="https://fonts.googleapis.com/css2?family=Open+Sans:wght@400;600;700;800&family=Montserrat:wght@700;800&display=swap">
<style>
:root{
  --blue:#3176b5;
  --blue-mid:#85abd2;
  --blue-light:#cfdeed;
  --cream:#fdf1e2;
  --ink:#1d1d1d;
  --text:#333;
  --btn:#2b231e;
  --green:#2db84b;
  --grey:#8a8a8a;
  --white:#fff;
}
*{margin:0;padding:0;box-sizing:border-box}
html,body{width:1200px;height:4186px;overflow:hidden}
body{position:relative;background:var(--white);font-family:"Open Sans",Arial,sans-serif;color:var(--text)}
.abs{position:absolute}
/* header */
.logo{left:134px;top:40px;display:flex;flex-direction:column;align-items:center;gap:8px}
.logo-dot{width:56px;height:56px;border-radius:50%;background:var(--blue)}
.logo-name{font-family:"Montserrat",sans-serif;font-weight:700;font-size:26px;letter-spacing:2px;color:var(--ink)}
.nav{top:108px;left:385px;display:flex;font-size:17px;color:#555}
.nav a{text-decoration:none;color:inherit;position:absolute;white-space:nowrap}
.nav .active{color:var(--blue);text-decoration:underline}
/* hero */
.hero{top:162px;left:0;width:1200px;height:468px}
.hero-sea{position:absolute;left:0;top:0;width:586px;height:468px;background:linear-gradient(180deg,#6fb2e8 0%,#9fd0f2 35%,#2f6fa5 55%,#3c3a36 100%)}
.hero-meet{position:absolute;left:586px;top:0;width:614px;height:468px;background:linear-gradient(135deg,#3a3a3c 0%,#8b8680 45%,#c9c4bc 70%,#5b4a3c 100%)}
.hero-title{position:absolute;left:0;width:1200px;top:252px;text-align:center;padding-left:40px;font-family:"Montserrat",sans-serif;font-weight:800;font-size:46px;color:var(--white);letter-spacing:1px}
.hero-btn{position:absolute;left:483px;top:382px;width:217px;height:40px;border-radius:8px;background:var(--cream);border:2px solid var(--btn);font-weight:700;font-size:15px;color:var(--ink);display:flex;align-items:center;justify-content:center}
.hero-dots{position:absolute;left:1178px;top:360px;display:flex;flex-direction:column;gap:14px}
.hero-dots span{width:10px;height:10px;border-radius:50%;background:var(--white);opacity:.8}
/* headings */
.h-main{left:134px;top:662px;font-family:"Montserrat",sans-serif;font-weight:800;font-size:21px;color:var(--ink);letter-spacing:.3px}
.band{left:0;width:1200px;background:var(--cream)}
.band-intro{top:698px;height:362px;padding:20px 134px}
.sub{font-weight:700;font-size:14px;color:var(--ink);letter-spacing:.3px}
.para{font-size:15px;line-height:1.45;color:var(--text);margin-top:10px}
.checks{list-style:none;margin-top:22px}
.checks li{font-size:15px;margin-bottom:12px;display:flex;align-items:center;gap:6px}
.checks li::before{content:"";width:12px;height:12px;border-radius:50%;background:var(--green)}
.dark-btn{height:73px;border-radius:37px;background:var(--btn);box-shadow:inset 0 0 0 4px var(--btn),inset 0 0 0 7px var(--white);color:var(--white);font-weight:700;font-size:19px;display:flex;align-items:center;justify-content:center}
.h-center{left:0;width:1200px;text-align:center;font-family:"Montserrat",sans-serif;font-weight:800;color:var(--ink)}
.why-icon{width:140px;height:140px;border-radius:50%;border:3px solid #888;background:var(--white)}
.why-icon div{position:absolute;left:28px;top:28px;width:78px;height:78px;border-radius:50%}
.card{top:1437px;width:234px;height:215px;background:var(--cream);border-radius:26px;padding:28px 22px;font-size:15px;color:var(--ink);display:flex;flex-direction:column;justify-content:space-between;text-transform:uppercase}
.card.center{text-align:center}
.partner{top:1735px;height:274px;padding:34px 230px;text-align:center;font-size:14px;line-height:1.4}
.partner p+p{margin-top:18px}
.photo-round{border-radius:50%;overflow:hidden}
/* calculator */
.calc-label{font-size:20px;color:var(--ink);text-align:center;line-height:1.15;width:400px}
.slider{left:446px;top:3824px;display:flex;gap:7px}
.slider span{width:50px;height:7px;border-radius:4px;background:#d8d2c8}
.slider span.on{background:var(--ink)}
.toggle{top:3882px;width:62px;height:22px;border-radius:11px}
.toggle::after{content:"";position:absolute;top:-3px;width:28px;height:28px;border-radius:50%}
.toggle.yes{background:var(--green)}
.toggle.yes::after{left:0;background:var(--green);box-shadow:0 0 0 2px #1f8f37}
.toggle.no{background:var(--grey)}
.toggle.no::after{left:0;background:#666}
.tlabel{top:3918px;font-size:14px;font-weight:600;width:120px;text-align:center}
/* footer */
.footer{top:4018px;height:168px;text-align:center;font-size:14px;color:var(--ink);line-height:29px;padding-top:8px}
.social{top:4150px;width:28px;height:28px;border-radius:50%;border:2px solid var(--ink)}
</style>
</head>
<body>

<header>
  <div class="abs logo"><span class="logo-dot"></span><span class="logo-name">FRIBRIX</span></div>
  <nav class="abs nav">
    <a class="active" style="left:0">Hem</a>
    <a style="left:123px">Jobba som egenanställd</a>
    <a style="left:363px">Företag</a>
    <a style="left:494px">Om oss</a>
    <a style="left:628px">Logga in</a>
  </nav>
</header>

<section class="abs hero">
  <div class="hero-sea" role="img" aria-label="Person med utsträckta armar vid havet"></div>
  <div class="hero-meet" role="img" aria-label="Affärsmöte med handslag vid ett bord"></div>
  <div class="hero-title">YOU CAN DO IT SOLO</div>
  <div class="hero-btn">Bli Soloföretagare</div>
  <div class="hero-dots"><span></span><span></span><span></span></div>
</section>

<h1 class="abs h-main">FAKTURERA UTAN EGET FÖRETAG, ANLITA MEDARBETARE UTAN ATT ANSTÄLLA</h1>
<section class="abs band band-intro">
  <p class="sub">FOKUSERA PÅ ATT UTFÖRA UPPDRAGET SÅ TAR VI HAND OM RESTEN</p>
  <p class="para">Fribrix är ett egenanställningsföretag som förenklar, effektiviserar och tryggar administrationen och hjälper dig som egen att fakturera utan att behöva ett eget företag. Slipp administrationen och fokusera på det du gör bäst. Läs mer…</p>
  <ul class="checks">
    <li>Vi hanterar fakturering, skatter, avgifter och moms åt dig som egenanställd</li>
    <li>Vi erbjuder ett heltäckande försäkringsskydd</li>
    <li>Vi sköter utbetalning av din lön och bevakning av dina kundfakturor så att du får betalt</li>
    <li>Få möjlighet till expressbetalning inom 24 timmar</li>
  </ul>
  <p class="sub" style="margin-top:4px">VÄLJ UT OCH ANLITA DINA KOMPETENTA MEDARBETARE UTAN ATT ANSTÄLLA</p>
  <p class="para">För företag och privatpersoner erbjuder Fribrix möjligheten att anlita medarbetare utan att behöva anställa. Du väljer medarbetare och Fribrix tar hela arbetsgivaransvaret. Vi förenklar och effektiviserar din hantering av externa medarbetare. Läs mer…</p>
</section>

<div class="abs dark-btn" style="left:167px;top:1096px;width:355px">Jobba som egenanställd</div>
<div class="abs dark-btn" style="left:689px;top:1096px;width:354px">Anlita Medarbetare</div>

<h2 class="abs h-center" style="top:1236px;font-size:16px">VARFÖR FRIBRIX?</h2>
<div class="abs why-icon" style="left:209px;top:1264px"><div role="img" aria-label="Ikon med band" style="background:#f2a23a"></div></div>
<div class="abs why-icon" style="left:530px;top:1264px"><div role="img" aria-label="Ikon med hand och sedel" style="background:#27b24a"></div></div>
<div class="abs why-icon" style="left:870px;top:1264px"><div role="img" aria-label="Ikon med handslag" style="background:var(--blue)"></div></div>

<div class="abs card" style="left:159px"><span>Beprövat lönesystem</span><span>Erfarna medarbetare</span><span>Väletablerade kontakter</span></div>
<div class="abs card center" style="left:483px"><span>Endast 3,95 % avgift</span><span>Kostnadsfritt konto</span><span>Möjlighet till express betalning</span></div>
<div class="abs card" style="left:817px"><span>Fakturera utan företag</span><span>Enkla villkor</span><span>Vi tar hand om all administration</span></div>

<h2 class="abs h-center" style="top:1693px;font-size:19px">FRIBRIX EN TRYGG PARTNER</h2>
<section class="abs band partner">
  <p>Fribrix är ett egenanställningsföretag som ger människor möjlighet att nå sina drömmar och arbeta som egenföretagare utan eget företag. Vi frigör tid och skapar trygghet genom att ta hand om administrationen.</p>
  <p>Fribrix startade 2016 och ingår i Veridan-koncernen. Veridan har fått utmärkelser som Topplistföretag av Näringsbladet, Snabbväxare av Berglund &amp; Partners och Tillväxtföretag av Affärstidningen. Sedan 2008 har Veridan dessutom en AAA-klassning från Kreditkollen. Vi är helt enkelt en koncern med ordning på vår ekonomi.</p>
  <p>Veridan grundades 2003 av Erik Lindmark och Anton Sjöberg som är rutinerade entreprenörer med erfarenhet av konsultverksamhet sedan 1996. Erik är idag Veridans koncernchef och Anton är styrelseordförande. http://www.veridan.se/om-oss/</p>
</section>

<h2 class="abs h-center" style="top:2094px;font-size:15px">FOKUSERA PÅ DET DU ÄR BRA PÅ!</h2>
<div class="abs" style="left:134px;top:2135px;width:932px;height:628px;overflow:hidden">
  <div class="photo-round" role="img" aria-label="Collage av glada yrkespersoner i svartvitt och färg" style="position:absolute;left:0;top:-150px;width:932px;height:932px;background:linear-gradient(90deg,#2a2a2a 0%,#cfcfcf 18%,#3b2d24 30%,#a08468 45%,#e8e4de 55%,#6a5a4c 70%,#d9d4cc 82%,#404040 100%)"></div>
</div>
<div class="abs dark-btn" style="left:413px;top:2740px;width:368px;height:78px;font-size:18px">Vi hjälper dig med resten!</div>

<h2 class="abs h-center" style="top:2892px;font-size:15px">FÖLJ FRIBRIX PÅ INSTAGRAM</h2>
<div class="abs" style="left:134px;top:2958px;width:940px;height:558px;overflow:hidden">
  <div class="photo-round" role="img" aria-label="Bildflöde med porträtt av frilansare" style="position:absolute;left:0;top:-382px;width:940px;height:940px;background:linear-gradient(90deg,#e4ddd2 0%,#6b5a46 20%,#f0f0f0 30%,#3a3a3a 45%,#8e8e8e 58%,#2c2c2c 70%,#c8c8c8 84%,#1e1e1e 100%)"></div>
</div>

<h2 class="abs h-center" style="top:3574px;font-size:19px;font-family:'Open Sans',sans-serif;font-weight:700">Räkna ut din lön!</h2>
<div class="abs calc-label" style="left:143px;top:3702px">Fakturabelopp exkl. moms<br>10 000 SEK</div>
<div class="abs calc-label" style="left:629px;top:3702px">Din nettolön<br>5 116 SEK</div>
<div class="abs slider"><span></span><span class="on"></span><span></span><span></span><span></span><span></span><span></span></div>
<div class="abs" style="left:443px;top:3843px;font-size:15px;color:var(--ink)">Ålder</div>
<div class="abs toggle yes" style="left:466px"></div>
<div class="abs toggle no" style="left:669px"></div>
<div class="abs tlabel" style="left:437px;color:var(--green)">Över 65</div>
<div class="abs tlabel" style="left:640px;color:var(--grey)">Under 65</div>

<footer class="abs band footer">
  <div>Fribrix AB</div>
  <div>Solbergsgatan 8</div>
  <div>118 20 Stockholm, Sverige</div>
  <div>Tel: 08-555 012 34, info@fribrix.se</div>
  <div>© 2018 FRIBRIX</div>
</footer>
<span class="abs social" style="left:996px"></span>
<span class="abs social" style="left:1032px"></span>

</body>
</html>
```